Larkspur Invitation

Please have the invitation say this
You're Invited to Our End-of-Summer Soirée!

As the summer winds down, we’d love for you to join us for a special evening of networking and good company, hosted by Larkspur Realty and Marcus Pellow with Brightvale Mortgage Solutions.

Date: September 19th, 2024
Time: 4:00 PM - 6:00 PM
Location: The Quillmere by Ashford Boston Downtown, Fennick Yard Kitchen and Bar

We’re offering complimentary drinks, light bites, and an exciting raffle with a fantastic prize up for grabs! So come unwind, connect with fellow professionals, and enjoy a relaxing time together.

We can’t wait to see you there and share a toast to new opportunities!

Please RSVP by September 5th by emailing tamsin@larkspurnorth.example

Please include the Quillmere Hotel Logo, Larkspur Logo and Brightvale Mortgage Solutions Logo. This should be a very classy invitation using navy and gold colors. Possibly herringbone pattern and aesthetic

```html
<!DOCTYPE html>
<html lang="en">
<head>
<meta charset="utf-8">
<title>Larkspur Invitation – End-of-Summer Soirée</title>
<link rel="stylesheet" href="https://fonts.googleapis.com/css2?family=Montserrat:wght@400;500;700;800;900&display=swap">
<style>
  :root {
    --navy: #0f2347;
    --navy-deep: #0a1a38;
    --navy-light: #1a3263;
    --gold: #e2b64a;
    --gold-light: #f3d27a;
    --gold-dark: #b8892a;
    --white: #ffffff;
    --marble: #f3f3f1;
    --marble-vein: #dcdcd8;
  }
  * { box-sizing: border-box; margin: 0; padding: 0; }
  html, body {
    width: 849px; height: 1200px; overflow: hidden;
    font-family: "Montserrat", Arial, sans-serif;
  }
  .invitation {
    position: relative;
    width: 849px; height: 1200px;
    overflow: hidden;
  }
  .marble-backdrop {
    position: absolute; inset: 0;
    background: linear-gradient(135deg, var(--marble) 0%, var(--white) 35%, var(--marble-vein) 55%, var(--white) 75%, var(--marble) 100%);
  }
  .panel {
    position: absolute;
    left: 78px; top: 0;
    width: 693px; height: 1040px;
    background: linear-gradient(180deg, var(--navy-light) 0%, var(--navy) 45%, var(--navy-deep) 100%);
    box-shadow: 0 8px 24px rgba(10, 26, 56, 0.35);
  }
  .panel-texture {
    position: absolute; inset: 0;
    background: radial-gradient(ellipse at 50% 20%, rgba(255,255,255,0.06), transparent 70%);
  }
  .gold-edge {
    position: absolute; top: 0; bottom: 0; width: 12px;
    background: linear-gradient(180deg, var(--gold-light), var(--gold) 40%, var(--gold-dark) 100%);
  }
  .gold-edge--left { left: 0; }
  .gold-edge--right { right: 0; }
  .gold-edge::after {
    content: ""; position: absolute; top: 0; bottom: 0; width: 2px;
    background: var(--gold-light);
  }
  .gold-edge--left::after { right: -6px; }
  .gold-edge--right::after { left: -6px; }

  .content {
    position: relative;
    padding: 50px 60px 0;
    text-align: center;
    color: var(--white);
  }
  .headline {
    font-weight: 900;
    font-size: 56px;
    line-height: 1.05;
    text-transform: uppercase;
    letter-spacing: 0.5px;
  }
  .headline .accent { color: var(--gold); }
  .intro {
    margin: 40px auto 0;
    width: 480px;
    font-size: 12.5px;
    line-height: 1.5;
  }
  .details {
    display: flex;
    justify-content: center;
    gap: 80px;
    margin-top: 34px;
    text-align: left;
  }
  .label {
    color: var(--gold);
    font-weight: 800;
    font-size: 32px;
    text-transform: uppercase;
    line-height: 1.05;
  }
  .value {
    font-weight: 800;
    font-size: 32px;
    text-transform: uppercase;
    line-height: 1.05;
  }
  .location {
    margin: 38px auto 0;
    width: 470px;
    font-weight: 800;
    font-size: 17px;
    line-height: 1.35;
    text-transform: uppercase;
  }
  .location .label { font-size: 17px; display: inline; }
  .offer {
    margin: 12px auto 0;
    width: 440px;
    font-size: 12.5px;
    line-height: 1.5;
  }
  .toast {
    margin: 70px auto 0;
    width: 490px;
    color: var(--gold);
    font-weight: 500;
    font-size: 27px;
    line-height: 1.12;
    text-transform: uppercase;
  }
  .rsvp {
    margin-top: 58px;
    font-weight: 800;
    text-transform: uppercase;
    line-height: 1.15;
  }
  .rsvp-lead { font-size: 23px; }
  .rsvp-deadline { font-size: 27px; }
  .rsvp-email { font-size: 22px; }

  .partners {
    position: absolute;
    left: 78px; right: 78px; top: 1070px;
    display: flex;
    justify-content: space-between;
    align-items: center;
    padding: 0 20px;
  }
  .partner {
    display: flex; align-items: center; gap: 10px;
    color: var(--navy);
    font-weight: 700;
    font-size: 22px;
    letter-spacing: 1px;
  }
  .partner-mark {
    width: 64px; height: 64px; border-radius: 50%;
    background: var(--navy);
  }
</style>
</head>
<body>
<main class="invitation">
  <div class="marble-backdrop" role="img" aria-label="White marble texture background"></div>

  <section class="panel">
    <div class="panel-texture" role="img" aria-label="Subtle navy herringbone pattern"></div>
    <div class="gold-edge gold-edge--left"></div>
    <div class="gold-edge gold-edge--right"></div>

    <div class="content">
      <h1 class="headline">You're<br>invited to our<br><span class="accent">End-of-Summer</span><br>Soirée!</h1>

      <p class="intro">As the summer winds down, we’d love for you to join us for a special evening of networking and good company, hosted by Larkspur Realty and Marcus Pellow with Brightvale Mortgage Solutions.</p>

      <div class="details">
        <div class="details-item">
          <div class="label">Date:</div>
          <div class="value">September<br>19th, 2024</div>
        </div>
        <div class="details-item">
          <div class="label">Time:</div>
          <div class="value">4:00 PM -<br>6:00 PM</div>
        </div>
      </div>

      <p class="location"><span class="label">Location:</span> The Quillmere by Ashford Boston Downtown, Fennick Yard Kitchen and Bar</p>

      <p class="offer">We’re offering complimentary drinks, light bites, and an exciting raffle with a fantastic prize up for grabs! So come unwind, connect with fellow professionals, and enjoy a relaxing time together.</p>

      <p class="toast">We can’t wait to see you there and share a toast to new opportunities!</p>

      <div class="rsvp">
        <p class="rsvp-lead">Please RSVP by</p>
        <p class="rsvp-deadline">September 5th by emailing</p>
        <p class="rsvp-email">tamsin@larkspurnorth.example</p>
      </div>
    </div>
  </section>

  <footer class="partners">
    <div class="partner partner--brightvale"><span class="partner-mark"></span>Brightvale</div>
    <div class="partner partner--larkspur">Larkspur Realty</div>
    <div class="partner partner--quillmere">Quillmere</div>
  </footer>
</main>
</body>
</html>
```